Wedding invitation

We need a wedding invitation designed with a logo using our initials and name underneath.
We are getting married at THE BRENNA hotel in Gstaad and we would like have our logo similar to theirs but incorporating our initials n&g (any font/case) and our names below noreen and Gilberto. THE BRENNA logo can be seen on their website.
The invitation would be square with the logo on the front in stamped foil and the colour would be THE BRENNA brown (I have the exact colour)
THE BRENNA Brown: C45 M70 Y68 K77
THE BRENNA Rose Gold: VELMAR 218
Inside we would have the invitation wording and on the opposite side some contact info. There would be four inserts - accom, directions, brunch and RSVP. We will provide the wording.

```html
<!DOCTYPE html>
<html lang="en">
<head>
<meta charset="utf-8">
<title>Brunch Invitation – Noreen and Gilberto</title>
<link rel="stylesheet" href="https://fonts.googleapis.com/css2?family=Great+Vibes&family=Tinos&display=swap">
<style>
  :root {
    --paper: #ffffff;
    --rose: #b26a74;
    --rose-soft: #e9ccd0;
    --rose-pale: #f6e9eb;
    --ink-brown: #2b1912;
  }
  * { margin: 0; padding: 0; box-sizing: border-box; }
  html, body {
    width: 1200px;
    height: 1200px;
    overflow: hidden;
    background: var(--paper);
  }
  .invitation {
    position: relative;
    width: 1200px;
    height: 1200px;
    background: var(--paper);
    font-family: "Tinos", "Times New Roman", serif;
    color: var(--rose);
  }
  .frame { position: absolute; inset: 0; }
  .corner-flourish {
    position: absolute;
    width: 172px;
    height: 172px;
    border-radius: 40px;
    background: radial-gradient(circle at center, var(--rose-soft) 0%, var(--rose-pale) 70%, rgba(246,233,235,0) 100%);
  }
  .corner-flourish--tl { left: 18px; top: 18px; }
  .corner-flourish--tr { right: 18px; top: 18px; }
  .corner-flourish--bl { left: 18px; bottom: 18px; }
  .corner-flourish--br { right: 18px; bottom: 18px; }

  .line { position: absolute; text-align: center; left: 0; right: 0; line-height: 1; }
  .title {
    top: 82px;
    font-family: "Great Vibes", cursive;
    font-size: 100px;
    color: var(--ink-brown);
  }
  .title-flourish {
    position: absolute;
    left: 382px; top: 200px;
    width: 400px; height: 60px;
    border-radius: 30px;
    background: linear-gradient(90deg, rgba(233,204,208,0), var(--rose-soft) 25%, var(--rose-soft) 75%, rgba(233,204,208,0));
  }
  .body-text { font-size: 29px; }
  .hosts { top: 343px; }

  .couple {
    position: absolute;
    top: 400px; left: 0; right: 0;
    height: 150px;
    font-family: "Great Vibes", cursive;
    color: var(--ink-brown);
  }
  .couple__name { position: absolute; font-size: 76px; line-height: 1; }
  .couple__name--first { left: 290px; top: 18px; }
  .couple__joiner { position: absolute; left: 490px; top: 48px; font-size: 50px; line-height: 1; }
  .couple__name--second { left: 610px; top: 60px; }

  .request { top: 594px; }
  .vows { top: 646px; }
  .date { top: 693px; }

  .divider {
    position: absolute;
    left: 458px; top: 762px;
    width: 236px; height: 6px;
    border-radius: 3px;
    background: linear-gradient(90deg, rgba(178,106,116,0), var(--rose) 50%, rgba(178,106,116,0));
  }
  .meal-time { top: 793px; }
  .scroll-ornament {
    position: absolute;
    left: 493px; top: 860px;
    width: 168px; height: 34px;
    border-radius: 17px;
    background: var(--rose-soft);
  }
  .address-street { top: 922px; }
  .address-town { top: 967px; }
  .reception-note { top: 1059px; }
</style>
</head>
<body>
<main class="invitation">
  <svg class="frame" width="1200" height="1200" viewBox="0 0 1200 1200" aria-hidden="true">
    <g stroke="var(--rose)" fill="none">
      <line x1="197" y1="27" x2="998" y2="27" stroke-width="3"/>
      <line x1="197" y1="35" x2="998" y2="35" stroke-width="3"/>
      <line x1="197" y1="1165" x2="998" y2="1165" stroke-width="3"/>
      <line x1="197" y1="1173" x2="998" y2="1173" stroke-width="3"/>
      <line x1="27" y1="195" x2="27" y2="1003" stroke-width="3"/>
      <line x1="35" y1="195" x2="35" y2="1003" stroke-width="3"/>
      <line x1="1165" y1="195" x2="1165" y2="1003" stroke-width="3"/>
      <line x1="1173" y1="195" x2="1173" y2="1003" stroke-width="3"/>
    </g>
  </svg>
  <div class="corner-flourish corner-flourish--tl" role="img" aria-label="Ornamental swirl flourish, top left corner"></div>
  <div class="corner-flourish corner-flourish--tr" role="img" aria-label="Ornamental swirl flourish, top right corner"></div>
  <div class="corner-flourish corner-flourish--bl" role="img" aria-label="Ornamental swirl flourish, bottom left corner"></div>
  <div class="corner-flourish corner-flourish--br" role="img" aria-label="Ornamental swirl flourish, bottom right corner"></div>

  <h1 class="line title">Brunch</h1>
  <div class="title-flourish" role="img" aria-label="Looping ornamental flourish beneath the title"></div>

  <p class="line body-text hosts">Together with their parents</p>

  <div class="couple">
    <span class="couple__name couple__name--first">Noreen</span>
    <span class="couple__joiner">and</span>
    <span class="couple__name couple__name--second">Gilberto</span>
  </div>

  <p class="line body-text request">Request the honour of your presence</p>
  <p class="line body-text vows">As they exchange marriage vows</p>
  <p class="line body-text date">On Saturday, ....... March, 2014</p>

  <div class="divider" role="img" aria-label="Small ornamental divider"></div>

  <p class="line body-text meal-time">Brunch at Eleven thirty a.m</p>

  <div class="scroll-ornament" role="img" aria-label="Small scroll ornament"></div>

  <p class="line body-text address-street">Brennastrasse 23</p>
  <p class="line body-text address-town">3780 Gstaad, Switzerland</p>

  <p class="line body-text reception-note">Adult reception following ceremony</p>
</main>
</body>
</html>
```